Recycling Exhibition Web Design Project

We are developing a new website for a exhibition we have just taken over. The previous site is very basic and we require a complete redesign. The site should be designed to engage with and attract those who work in or provide services to the multibillion dollar wastes and recycling industry in the Asia pacific region. These will include Federal & State Governments, City councils, private sector, industry associations and other key bodies, education facilities.

PLTX is the premier waste and recycling event in the Asia Pacific region and known as place where the industry meets to share innovations, gain knowledge, to network and do business.
• Innovation
• Knowledge transfer
• Industry Networking
• Trade
Key point: need to reflect that 2012 show will attract large numbers of quality visitors from across wide range of the industry – city councils, facilities managers, etc

Site should deliver 3 key objectives.
1. Stimulate interest those who work in or provide services to the wastes and recycling industry by providing simple to access, relevant and topical information about the Expo, the Seminars, the Key Features, the sub activities and the key benefits to them.
2. Provide a platform that supports / improves EP by providing a range of interactive components – ie floor plan / video. In addition options for sales enquiries, registration, general feedback
3. Provide a way to highlight / showcase sponsors, show features and other key assets. (possibly a carousel above the fold)

We really like the korba website so a take on this could be good (http://www.korba-example.com.au/). Also we want to try to reinforce the brand so we should use the event as the hero image/banner.

Previous website - http://www.pltx-example.com.au/

Target Market(s)

The site should be designed to engage with and attract those who work in or provide services to the multibillion dollar wastes and recycling industry

Industry/Entity Type

Recycling

Requirements
Must have
• The icons on the current site work quite well so inclusion as CTAs would be preferable.

Other key areas are

• Seminar Delegate & Visitor Registration
• Exhibitor Prospectus
• Floorplan
• Conference / Seminar content
• Social media + blog

Site visitors will need to feel like they are part of a community.
Site should reflect/display key industry stats & stats from 2011 expo

Please see the attached brief for more details and site map for menu items.

```html
<!DOCTYPE html>
<html lang="en">
<head>
<meta charset="utf-8">
<title>Pacific Waste &amp; Recycling Expo 2012</title>
<link href="https://fonts.googleapis.com/css2?family=Play:wght@400;700&family=Open+Sans:wght@400;600&display=swap" rel="stylesheet">
<style>
:root{
  --paper:#e9e9e9;
  --page:#f4f4f4;
  --ink:#1d1d1d;
  --dark:#3c3c3c;
  --black:#222;
  --blue:#1aa9e6;
  --green:#1d8a3a;
  --teal:#1f7fb0;
  --orange:#e4542a;
}
*{margin:0;padding:0;box-sizing:border-box}
html,body{width:758px;height:1200px;overflow:hidden}
body{background:var(--paper);font-family:"Play",sans-serif;color:var(--ink);position:relative}
.page{position:absolute;left:76px;top:0;width:606px;height:1200px;background:var(--page)}
.abs{position:absolute}
/* header */
.logo-block{left:76px;top:10px;width:154px;height:83px;background:var(--black);display:flex;align-items:center;gap:6px;padding-left:10px}
.logo-block .dot{width:14px;height:14px;border-radius:50%;background:var(--orange);flex:none}
.logo-block span{color:#fff;font-size:15px;line-height:1.05;font-weight:700}
.date-band{left:230px;top:10px;width:452px;height:65px;background:var(--blue);text-align:right;padding:7px 8px 0 0;color:var(--ink)}
.date-band .date{font-size:21px;letter-spacing:1.5px;line-height:22px}
.date-band .venue{font-size:12.5px;letter-spacing:1px;line-height:14px}
.nav{left:230px;top:75px;width:452px;height:18px;display:flex;border-bottom:1px solid #bbb}
.nav a{font-family:"Open Sans",sans-serif;font-size:8.6px;color:var(--ink);text-decoration:none;padding:3px 7px 0}
.nav a.active{background:#fff}
/* carousel */
.slide{top:108px;height:122px}
.slide-side{background:linear-gradient(#888,#3a3a3a)}
.slide-main{left:225px;top:102px;width:310px;height:134px;background:linear-gradient(#6a7a4a,#3d4a2a 60%,#8a8a7a)}
.arrow-box{top:142px;width:74px;height:46px;background:#fff;box-shadow:0 1px 3px rgba(0,0,0,.4);display:flex;align-items:center;justify-content:center}
.headline{left:76px;top:246px;width:606px;text-align:center;font-size:23px;font-weight:400;letter-spacing:2px;line-height:28px}
/* cta */
.register{left:76px;top:314px;width:160px;height:63px;background:var(--blue);border:2px solid #fff;outline:1px solid var(--blue);font-weight:700;font-size:20px;line-height:26px;padding:5px 0 0;text-align:center;color:var(--black);letter-spacing:1px;text-decoration:none;white-space:nowrap}
.categories{left:242px;top:314px;width:440px;height:63px;display:flex}
.cat{flex:1;display:flex;flex-direction:column}
.cat .ico{height:40px;background:var(--black);display:flex;align-items:center;justify-content:center}
.cat .lbl{height:23px;background:var(--blue);font-family:"Open Sans",sans-serif;font-size:6.2px;text-align:center;line-height:7.5px;padding-top:3px;letter-spacing:-.2px}
/* body text */
.intro{left:86px;top:391px;width:590px;font-size:9px;letter-spacing:.5px;line-height:10.5px}
.bar-head{background:var(--dark);color:#fff;font-weight:400;letter-spacing:1.5px}
.says{left:76px;top:420px;width:393px;height:18px;padding:2px 0 0 11px;font-size:12px}
.quote{left:86px;width:590px;font-size:8.5px;font-style:italic;letter-spacing:.5px;line-height:10px}
.attrib{left:85px;font-size:9.5px;letter-spacing:.6px}
.stat{left:83px;width:600px}
.stat h3{font-weight:400;font-size:12.5px;letter-spacing:1.5px;line-height:14px}
.stat p{font-size:8.6px;letter-spacing:.5px;line-height:10px}
.teal{color:var(--teal)}.green{color:var(--green)}
/* topics */
.topics-title{left:88px;top:707px;font-size:21px;font-weight:400;letter-spacing:2px}
.topic{left:86px;width:400px;display:flex;gap:8px}
.topic svg{flex:none;margin-top:1px}
.topic h4{font-weight:400;color:var(--green);font-size:10px;letter-spacing:.8px;line-height:12px}
.topic p{font-size:8.6px;font-style:italic;letter-spacing:.5px;margin-top:5px}
.feat-head{left:87px;width:394px;height:27px;text-align:center;font-size:17px;line-height:27px;
  background:linear-gradient(to right,var(--dark) 0 13px,var(--page) 13px 16px,var(--dark) 16px calc(100% - 16px),var(--page) calc(100% - 16px) calc(100% - 13px),var(--dark) calc(100% - 13px))}
.feat-img{top:936px;width:118px;height:80px}
.feat-lbl{top:1025px;width:118px;text-align:center;font-size:11px;letter-spacing:1px}
.feat-lbl span{border-bottom:1px solid #888;padding-bottom:1px}
/* right column */
.side-head{left:492px;width:190px;height:28px;text-align:center;font-size:16px;line-height:28px;white-space:nowrap}
.quick{left:492px;width:190px;height:27px;background:var(--blue);color:#fff;font-size:12px;letter-spacing:1.5px;padding:5px 0 0 10px;text-decoration:none}
.social{top:1020px;width:17px;height:17px;background:#4a6fa5;border-radius:2px}
.sponsor{font-weight:700;font-size:30px;color:#1b4f9c}
.footer-line{left:76px;top:1168px;width:606px;border-top:1px solid #aaa}
.footer{top:1184px;font-size:8px;letter-spacing:.5px}
</style>
</head>
<body>
<div class="page"></div>

<header>
  <div class="abs logo-block"><div class="dot"></div><span>Pacific Waste<br>&amp; Recycling Expo</span></div>
  <div class="abs date-band">
    <div class="date">21 - 22 NOVEMBER 2012</div>
    <div class="venue">Harbourside Convention Centre</div>
    <div class="venue">Bayfront Quay</div>
  </div>
  <nav class="abs nav">
    <a class="active" href="#">HOME</a><a href="#">ABOUT THE SHOW</a><a href="#">WHAT'S ON</a><a href="#">REGISTER</a><a href="#">HOW TO EXIBIT</a><a href="#">BLOG</a><a href="#">CONTACT US</a>
  </nav>
</header>

<section class="carousel">
  <div class="abs slide slide-side" style="left:104px;width:121px" role="img" aria-label="Dark recycling bin close-up"></div>
  <div class="abs slide slide-side" style="left:535px;width:120px;background:linear-gradient(#ccc,#555)" role="img" aria-label="Harbour skyline in black and white"></div>
  <div class="abs slide-main" role="img" aria-label="Green glass bottle lying on a heap of recycled glass"></div>
  <div class="abs arrow-box" style="left:82px"><svg width="46" height="28" viewBox="0 0 46 28"><path d="M22 2 8 14l14 12M40 2 26 14l14 12" fill="none" stroke="#111" stroke-width="6"/></svg></div>
  <div class="abs arrow-box" style="left:603px"><svg width="46" height="28" viewBox="0 0 46 28"><path d="M6 2l14 12L6 26M24 2l14 12-14 12" fill="none" stroke="#111" stroke-width="6"/></svg></div>
</section>

<h1 class="abs headline">WANT TO KNOW WHAT IS NEXT IN<br>WASTE, RECYCLING AND SUSTAINABILITY?</h1>

<a class="abs register" href="#">CLICK HERE<br>REGISTER NOW</a>
<div class="abs categories">
  <div class="cat"><div class="ico"><svg width="28" height="26"><path d="M14 2 27 24H1z" fill="none" stroke="#b33" stroke-width="3"/></svg></div><div class="lbl">HAZARDOUS<br>WASTE</div></div>
  <div class="cat"><div class="ico"><svg width="28" height="26"><rect x="6" y="6" width="16" height="16" fill="var(--orange)" transform="rotate(20 14 14)"/></svg></div><div class="lbl">DISPOSAL</div></div>
  <div class="cat"><div class="ico"><svg width="28" height="26"><circle cx="14" cy="15" r="9" fill="var(--orange)"/></svg></div><div class="lbl">COMPOST</div></div>
  <div class="cat"><div class="ico"><svg width="28" height="26"><circle cx="14" cy="10" r="7" fill="none" stroke="#c8d84a" stroke-width="2.5"/><rect x="11" y="18" width="6" height="6" fill="#c8d84a"/></svg></div><div class="lbl">ENERGY<br>FROM WASTE</div></div>
  <div class="cat"><div class="ico"><svg width="28" height="26"><path d="M8 6h12l-2 18h-8z" fill="#c33"/></svg></div><div class="lbl">BIN LINERS<br>&amp; CONTAINERS</div></div>
  <div class="cat"><div class="ico"><svg width="28" height="26"><circle cx="10" cy="14" r="7" fill="none" stroke="var(--orange)" stroke-width="4"/><circle cx="20" cy="12" r="6" fill="none" stroke="var(--orange)" stroke-width="4"/></svg></div><div class="lbl">MACHINERY<br>&amp; EQUIPMENT</div></div>
  <div class="cat"><div class="ico"><svg width="28" height="26"><path d="M3 5l11 3 11-3v18l-11 3-11-3z" fill="#f08a2a"/></svg></div><div class="lbl">SERVICE<br>&amp; SOLUTIONS</div></div>
  <div class="cat"><div class="ico"><svg width="30" height="26"><rect x="2" y="7" width="18" height="13" fill="#9c3"/><path d="M20 11h6l3 4v5h-9z" fill="#9c3"/></svg></div><div class="lbl">VEHICLES<br>&amp; PLANTS</div></div>
  <div class="cat"><div class="ico"><svg width="28" height="26"><path d="M14 3 22 17H6z" fill="none" stroke="#5a5" stroke-width="3.5"/></svg></div><div class="lbl">RECYCLED<br>PRODUCTS</div></div>
</div>

<p class="abs intro">THANK YOU to all who participated in the second Pacific Waste &amp; Recycling Expo.&nbsp; The event was a huge success with over 1600 industry professionals registering from more than 800 organisations and 16 countries.</p>

<h2 class="abs bar-head says">WHAT OUR&nbsp; EXHIBITORS AND DELEGATES HAVE TO SAY....</h2>
<p class="abs quote" style="top:444px">"PLTX was the perfect venue for us to launch our new organics units. In this digital era, being able to speak face-to-face and show visitors how the units work really helped them to understand the benefits. The quality and quantity of the visitors was just what we were looking for."</p>
<p class="abs attrib" style="top:481px">LOOPWISE - 2011 EXIBITOR</p>
<p class="abs quote" style="top:497px">"I found our firm's participation in the 2011 PLTX conference rewarding given the opportunity to engage with colleagues and potential customers in the waste to energy industry.&nbsp; My attendance has led to business leads and to continued exposure to government and private sector&nbsp; interests in other venues."</p>
<p class="abs attrib" style="top:533px">Kestrel Energy Pty Ltd - 2011 DELEGATE</p>

<div class="abs stat" style="top:558px"><h3 class="teal">TRADE SHOW</h3><p>95 exhibitors from the U.S, U.K, NZ &amp; Australia filled Hall 5 at the Harbourside Convention Centre.</p></div>
<div class="abs stat" style="top:590px"><h3 class="green">FULL CONFERENCE</h3><p>Daniel Marsh, MP delivered the keynote address. More than 350 professionals registered for one or more of the four half day conference sessions.</p></div>
<div class="abs stat" style="top:632px"><h3 class="green">FREE WORKSHOPS</h3><p>Over 120 people enjoyed one of the free workshops held.</p></div>
<div class="abs stat" style="top:665px"><h3 class="green">NETWORKING FUNCTIONS</h3><p>The Hon. Helen Carver, MP&nbsp; opened the networking function attended by 400 sustainability professionals.</p></div>

<h2 class="abs topics-title">CONFERENCE TOPICS:</h2>
<div class="abs topic" style="top:745px"><svg width="12" height="12"><circle cx="6" cy="6" r="5" fill="none" stroke="#333" stroke-width="2"/></svg><div><h4>IMPACT OF THE CARBON PRICE &amp; CARBON FARMING INITIATIVE</h4><p>Daniel Marsh, Federal MP is presenting.</p></div></div>
<div class="abs topic" style="top:783px"><svg width="12" height="12"><circle cx="6" cy="6" r="5" fill="none" stroke="#333" stroke-width="2"/></svg><div><h4>PRODUCT STEWARDSHIP &amp; INNOVATION</h4><p>Product Stewardship Act 2011 and TV &amp; Computer scheme explained.</p></div></div>
<div class="abs topic" style="top:819px"><svg width="12" height="12"><circle cx="6" cy="6" r="5" fill="none" stroke="#333" stroke-width="2"/></svg><div><h4>WASTE TO ENERGY &amp; LOCAL GOVERNMENT AWT PROCUREMENT</h4><p>New waste to energy projects in Australia. Solace Energy &amp; Coral Pyrolysis.</p></div></div>
<div class="abs topic" style="top:856px"><svg width="12" height="12"><circle cx="6" cy="6" r="5" fill="none" stroke="#333" stroke-width="2"/></svg><div><h4>GREEN BUILDINGS</h4><p>New 6 Stars GREENRATE &amp; the latest in green design.</p></div></div>

<h2 class="abs bar-head feat-head" style="top:897px">SHOW FEATURES</h2>
<div class="abs feat-img" style="left:94px;background:linear-gradient(#6b4a2a,#8a3a20)" role="img" aria-label="Audience at a seminar session"></div>
<div class="abs feat-img" style="left:225px;background:linear-gradient(#4a6070,#6a5a50)" role="img" aria-label="Exhibition hall featured area"></div>
<div class="abs feat-img" style="left:355px;background:linear-gradient(#7ac234,#4e9a1c)" role="img" aria-label="Green reusable shopping bag product"></div>
<div class="abs feat-lbl" style="left:94px"><span>SEMINARS</span></div>
<div class="abs feat-lbl" style="left:225px"><span>FEATURED AREAS</span></div>
<div class="abs feat-lbl" style="left:355px"><span>NEW PRODUCTS</span></div>

<h2 class="abs bar-head feat-head" style="top:1053px">OUR SPONSORS</h2>
<svg class="abs" style="left:98px;top:1113px" width="24" height="28"><path d="M20 2 5 14l15 12" fill="none" stroke="#111" stroke-width="5"/></svg>
<svg class="abs" style="left:450px;top:1113px" width="24" height="28"><path d="M4 2l15 12L4 26" fill="none" stroke="#111" stroke-width="5"/></svg>
<div class="abs sponsor" style="left:150px;top:1103px">korba</div>
<div class="abs sponsor" style="left:282px;top:1106px;font-size:15px;line-height:17px;font-weight:400">State Office of<br>Environment</div>

<aside>
  <h2 class="abs bar-head side-head" style="top:705px">WATCH VIDEO</h2>
  <div class="abs" style="left:503px;top:738px;width:165px;height:100px;background:linear-gradient(#8aa9c8,#a07050)" role="img" aria-label="Video still from the expo"></div>
  <div class="abs" style="left:503px;top:838px;width:165px;height:9px;background:#333"><div style="margin:3px 0 0 15px;width:85px;height:3px;background:#c22"></div></div>
  <h2 class="abs bar-head side-head" style="top:852px;left:491px">VIEW FLOORPLAN</h2>
  <div class="abs" style="left:503px;top:883px;width:165px;height:110px;background:linear-gradient(135deg,#fff 0%,#9fcf8f 50%,#fff 100%);border:1px solid #ccc" role="img" aria-label="Exhibition hall floor plan"></div>
  <p class="abs" style="left:535px;top:994px;font-size:9px;letter-spacing:.5px">Click to see full plan..</p>
  <div class="abs social" style="left:498px"></div>
  <div class="abs social" style="left:525px;background:#3aa7d8"></div>
  <div class="abs social" style="left:555px;background:#2a77b5"></div>
  <div class="abs" style="left:585px;top:1020px;display:flex;align-items:center;gap:3px;font-size:9px"><span style="width:14px;height:14px;background:var(--green);display:inline-block"></span>greenlisting</div>
  <a class="abs quick" href="#" style="top:1048px">SALES ENQUIRIES</a>
  <a class="abs quick" href="#" style="top:1078px">REGISTRATION</a>
  <a class="abs quick" href="#" style="top:1108px">GENERAL FEEDBACK</a>
  <a class="abs quick" href="#" style="top:1138px">BLOG UPDATES</a>
</aside>

<footer>
  <div class="abs footer-line"></div>
  <p class="abs footer" style="left:84px">© 2012, Pacific Waste &amp; Recycling Expo</p>
  <p class="abs footer" style="left:511px;top:1187px;font-size:7.5px">brought to you by</p>
  <p class="abs" style="left:585px;top:1176px;font-size:15px;font-weight:700;color:#333">meridian</p>
</footer>
</body>
</html>
```